Information poster for parquet showroom

We are a parquet shop from germany and need some information poster for our showroom, to show our costumers some important information about parqut directly. The three posters are about reasons for parquet, and there are two types of paper on the subject. We would like to place the posters in a wooden frame. The design should be modern but simple. Enclosed I send you some of my ideas but it does not have to be like this. Can be completely different. I also send you some pictures of our showroom. 1st poster: Why parquet (dimension: 90x130 cm) Why parquet? - brings nature into your home - ecologically sustainable raw material - pleasantly warm - timeless% 26amp; high quality optics - durable% 26amp; reparable flooring - improved indoor climate - unique ride 2. Advantages oiled - tangible wood structure - natural appearance - scratches less present - partial repair possible advantage varnished - very easy-care - classic% 26amp; elegant appearance - protection against dirt and moisture - variable gloss level 3. Poster: overview of the hardness of different kinds of wood (dimension: 67x130 cm) wood hardness according to Brinell in N / mm² maple europ. 28 maple canadian. 35 birch 27 beech 33 oak 34 alder 17 ash 37 doussie 42 spruce 12 kambala 30 chestnut 18 pine 20 cherry european. 31 Larch 19 Merbau 44 Robinia 48 Sucupira 57 Elm 30 Wenge 45

```html
<!DOCTYPE html>
<html lang="en">
<head>
<meta charset="utf-8">
<title>Advantages Oiled</title>
<link href="https://fonts.googleapis.com/css2?family=Anton&family=Oswald:wght@700&display=swap" rel="stylesheet">
<style>
  :root {
    --bg-top: #121212;
    --bg-mid: #1c1c1c;
    --bg-bottom: #2e2e2e;
    --frame: #d9d9d9;
    --title: #e6e6e6;
    --subtitle: #6f6f6f;
    --item: #ececec;
    --bullet-front: #b5b5b5;
    --bullet-back: #5c5c5c;
  }
  * { margin: 0; padding: 0; box-sizing: border-box; }
  html, body { width: 831px; height: 1200px; overflow: hidden; background: var(--bg-top); }
  .poster {
    position: relative;
    width: 831px;
    height: 1200px;
    overflow: hidden;
  }
  .poster-background {
    position: absolute;
    inset: 0;
    background:
      linear-gradient(160deg, rgba(255,255,255,0.04) 0%, transparent 40%),
      linear-gradient(180deg, var(--bg-top) 0%, var(--bg-mid) 45%, var(--bg-bottom) 100%);
  }
  .poster-frame {
    position: absolute;
    left: 17px;
    top: 17px;
    width: 797px;
    height: 1165px;
    border: 1.5px solid var(--frame);
  }
  .title {
    position: absolute;
    left: 134px;
    top: 108px;
    font-family: "Anton", "Impact", sans-serif;
    font-size: 104px;
    line-height: 1;
    color: var(--title);
    letter-spacing: 1px;
    transform: rotate(-2.5deg);
    transform-origin: left center;
    white-space: nowrap;
  }
  .subtitle {
    position: absolute;
    left: 252px;
    top: 222px;
    font-family: "Anton", "Impact", sans-serif;
    font-size: 136px;
    line-height: 1;
    color: var(--subtitle);
    letter-spacing: 2px;
    transform: rotate(-8deg);
    transform-origin: left center;
    white-space: nowrap;
  }
  .advantage-list {
    list-style: none;
    position: absolute;
    left: 48px;
    top: 0;
  }
  .advantage-item {
    position: absolute;
    left: 0;
    display: flex;
    align-items: center;
    height: 40px;
    margin-top: -20px;
    white-space: nowrap;
    font-family: "Oswald", "Arial Narrow", sans-serif;
    font-weight: 700;
    font-size: 32px;
    letter-spacing: -0.4px;
    color: var(--item);
  }
  .bullet {
    position: relative;
    width: 26px;
    height: 26px;
    margin-right: 20px;
    flex: none;
  }
  .bullet::before,
  .bullet::after {
    content: "";
    position: absolute;
    width: 20px;
    height: 20px;
  }
  .bullet::before { left: 5px; top: 5px; background: var(--bullet-back); }
  .bullet::after  { left: 0; top: 0; background: linear-gradient(135deg, #d0d0d0, var(--bullet-front)); }
</style>
</head>
<body>
<div class="poster">
  <div class="poster-background" role="img" aria-label="Dark low-poly geometric pattern of charcoal triangles"></div>
  <div class="poster-frame"></div>

  <h1 class="title">ADVANTAGES</h1>
  <h2 class="subtitle">OILED</h2>

  <ul class="advantage-list">
    <li class="advantage-item" style="top:497px"><span class="bullet"></span>TANGIBLE WOOD STRUCTURE</li>
    <li class="advantage-item" style="top:574px"><span class="bullet"></span>NATURAL APPEARANCE</li>
    <li class="advantage-item" style="top:651px"><span class="bullet"></span>SCRATCHES LESS PRESENT</li>
    <li class="advantage-item" style="top:727px"><span class="bullet"></span>PARTIAL REPAIR POSSIBLE ADVANTAGE VARNISHED</li>
    <li class="advantage-item" style="top:805px"><span class="bullet"></span>VERY EASY-CARE</li>
    <li class="advantage-item" style="top:878px"><span class="bullet"></span>CLASSIC% 26AMP; ELEGANT APPEARANCE</li>
    <li class="advantage-item" style="top:949px"><span class="bullet"></span>PROTECTION AGAINST DIRT AND MOISTURE</li>
    <li class="advantage-item" style="top:1020px"><span class="bullet"></span>VARIABLE GLOSS LEVEL</li>
  </ul>
</div>
</body>
</html>
```